Company brochure for our unique consulting business

We are a small consulting business offering a unique set of services to our clients.. In simple terms we are a business improvement consultancy helping our clients get the best out of their businesses. We work with clients across multiple sectors and deliver a variety of services. We want to put together a brochure to cover these main themes:1. Who we are2. What we do3. The type of people we employ4. The sectors we work inWhile the brochure needs to have a certain corporate feel to it, we don't want it to be "boring" or "stiff". We would like it to have a slightly "friendly" or "informal" feel to it, to reflect the type of organisation we are.We have a company website http://tollandvergeadvisory.com , however we do not want to directly replicate the content or feel as we recognise it needs updating.We would like the brochure to be A4 portrait format. We anticipate requiring 12 sides (including covers) but we are happy to be guided on this based on the content we have provided.The attached ppt file gives the detail of the content to be included and also shows the proposed pagination. For the front cover we would like to try 2 versions, one with the TVA logo and one with the Tolland Verge Advisory logo (a file of both is attached)One of the most important pages will be the "Our Services" page. We would like this to cover the centre fold. In the ppt file we have shown an example layout, but this is where we need most help - we are clearly not graphic designers! This page will be the most used page in sales meetings etc.Also attached is the following:1. file for our TollandVerge Advisory company logo.2. File for our TVA company logo3. Files for Derek's signatures (for under photos) - Owen's to follow4. Photo of Derek & Owen (person in purple shirt to be cropped out)Thank you and really excited to see what everyone comes back with.Derek & Owen

Target Market(s)

Very broad - Manufacturing, Healthcare, Hospitality

Industry/Entity Type

Management Consulting

Font styles to use
Other font styles liked:
• We use Swiss721, but happy to be guided by designer

Colors
3276b5
85abd2
0355a3
333333
5c5c5c
9d9d9d
d9d9d9

Requirements
Must have
• Corporate feel
Nice to have
• Slightly friendly feel
• Our standard "blue" is (CORRECTION) - R55 G96 B146 #376092 and our standard grey is R197 G178, B179 - #B3B2B2, which we would like to keep, but other colours we are happy to be guided on. Brand guidelines attached.

```html
<!DOCTYPE html>
<html lang="en">
<head>
<meta charset="utf-8">
<title>Tolland Verge Advisory – Brochure Covers</title>
<link href="https://fonts.googleapis.com/css2?family=Montserrat:wght@400;600;700&display=swap" rel="stylesheet">
<style>
  :root {
    --backdrop: #666666;
    --paper: #ffffff;
    --navy: #23408e;
    --pale-blue: #cfdff0;
    --rule-blue: #cfdff0;
    --soft-blue: #6f9bd6;
    --ink: #111111;
    --photo-light: #e6e6e6;
    --photo-dark: #a9a9a9;
  }
  html, body {
    margin: 0;
    padding: 0;
    width: 1200px;
    height: 1200px;
    overflow: hidden;
    background: var(--backdrop);
    font-family: "Montserrat", sans-serif;
  }
  .spread {
    position: absolute;
    left: 32px;
    top: 198px;
    width: 1136px;
    height: 804px;
    background: var(--paper);
    overflow: hidden;
  }
  .rule {
    position: absolute;
    top: 181px;
    height: 2.5px;
    background: var(--rule-blue);
  }
  .rule--left { left: 0; width: 622px; }
  .rule--right { left: 944px; width: 192px; }

  .wordmark {
    position: absolute;
    left: 640px;
    top: 104px;
    width: 290px;
    text-align: center;
    font-weight: 700;
    font-size: 34px;
    line-height: 38px;
    letter-spacing: -0.5px;
    color: var(--ink);
    margin: 0;
  }

  .cover-block {
    position: absolute;
    left: 254px;
    top: 265px;
    width: 882px;
    height: 416px;
    background: var(--navy);
  }
  .cover-accent {
    position: absolute;
    left: 643px;
    top: 265px;
    width: 72px;
    height: 349px;
    background: var(--pale-blue);
  }
  .cover-photo {
    position: absolute;
    left: 715px;
    top: 265px;
    width: 421px;
    height: 349px;
    background: linear-gradient(160deg, var(--photo-light) 0%, #cfcfcf 55%, var(--photo-dark) 100%);
  }
  .web-band {
    position: absolute;
    left: 254px;
    top: 681px;
    width: 882px;
    height: 18px;
    background: var(--pale-blue);
  }
  .web-band__url {
    position: absolute;
    left: 9px;
    top: 4px;
    font-size: 7px;
    font-weight: 700;
    color: var(--navy);
  }

  .contact {
    position: absolute;
    left: 32px;
    top: 584px;
    color: var(--navy);
  }
  .contact__title {
    margin: 0 0 8px;
    font-size: 17px;
    font-weight: 700;
  }
  .contact__item {
    position: relative;
    padding-left: 24px;
    font-size: 11px;
    line-height: 13.5px;
    margin-bottom: 7px;
  }
  .contact__item--tight { margin-bottom: 3px; }
  .contact__icon {
    position: absolute;
    left: 0;
    top: 0;
    width: 14px;
    height: 14px;
  }

  .tagline {
    position: absolute;
    left: 660px;
    top: 725px;
    margin: 0;
    font-size: 11px;
    line-height: 14px;
    color: var(--soft-blue);
  }
</style>
</head>
<body>
  <main class="spread">
    <div class="rule rule--left"></div>
    <div class="rule rule--right"></div>

    <h1 class="wordmark">Tolland Verge<br>Advisory</h1>

    <div class="cover-block"></div>
    <div class="cover-accent"></div>
    <div class="cover-photo" role="img" aria-label="Black and white photo of the two founders smiling at a meeting table with a laptop"></div>
    <div class="web-band"><span class="web-band__url">www.tollandvergegroup.com</span></div>

    <section class="contact">
      <h2 class="contact__title">Contact Us</h2>
      <div class="contact__item">
        <svg class="contact__icon" viewBox="0 0 14 14" aria-hidden="true">
          <path d="M7 0.5C4.5 0.5 2.7 2.4 2.7 4.8 2.7 8 7 13.5 7 13.5S11.3 8 11.3 4.8C11.3 2.4 9.5 0.5 7 0.5Z" fill="#6f9bd6"/>
          <circle cx="7" cy="4.9" r="1.6" fill="#fff"/>
        </svg>
        TVA Limited<br>Wexmoor House<br>Kiln Lane, Harwick, HW4 2JN
      </div>
      <div class="contact__item contact__item--tight">
        <svg class="contact__icon" viewBox="0 0 14 14" aria-hidden="true">
          <circle cx="7" cy="7" r="6.5" fill="#6f9bd6"/>
          <path d="M4.6 3.6l1.3 1.4-.7 1c.5 1.1 1.3 1.9 2.4 2.4l1-.7 1.4 1.3-.9 1.2C6.7 10 4 7.3 3.4 4.5Z" fill="#fff"/>
        </svg>
        +44 (0) 1632 960418
      </div>
      <div class="contact__item">
        <svg class="contact__icon" viewBox="0 0 14 14" aria-hidden="true">
          <rect x="0.5" y="3" width="13" height="8.5" fill="#6f9bd6"/>
          <path d="M0.5 3L7 8l6.5-5" fill="none" stroke="#fff" stroke-width="1"/>
        </svg>
        enquiries@tollandvergegroup.com
      </div>
    </section>

    <p class="tagline">At TVA we constantly strive to deliver the best possible value for our clients.<br>Importantly we recognize, it’s our clients that define value, not us.</p>
  </main>
</body>
</html>
```